Fully Functional Wix Website, Not Just Images

Please read all instructions carefully. This is NOT merely a design project where the artist will deliver static images. This project requires that the designer build a fully functional SEO optimized website within Wix then transfer full ownership to me. See attached "instructions for design" file. I have wix for other websites. Only wix is acceptable. Do not submit more than 1 design per designer. If you submit more than 1 design I will award to someone else.

Target Market(s)

see attachments and trelvanox482.com

Industry/Entity Type

Coding

Coded - Design and coding required

Number of Pages Required

4 page

Font styles to use
Other font styles liked:
• see attachments and trelvanox482.com

Requirements
Must have
Nice to have
Should not have

```html
<!DOCTYPE html>
<html lang="en">
<head>
<meta charset="utf-8">
<title>Trelvanox482 — Gallery &amp; Contact</title>
<link href="https://fonts.googleapis.com/css2?family=Playfair+Display:wght@400;500;600;700&family=Manrope:wght@400;500;600;700&display=swap" rel="stylesheet">
<style>
:root{
  --ink:#141210;
  --body:#4a4540;
  --muted:#8d8780;
  --accent:#b4511f;
  --paper:#faf8f3;
  --stone:#f2f0eb;
  --panel:#edeae4;
  --line:#dedad3;
  --white:#ffffff;
  --serif:'Playfair Display',Georgia,serif;
  --sans:'Manrope',Arial,sans-serif;
}
*{box-sizing:border-box;margin:0;padding:0}
html,body{width:1200px;height:4406px;overflow:hidden}
body{background:var(--paper);font-family:var(--sans);color:var(--ink);position:relative}
.wrap{position:absolute;left:112px;right:112px}
.eyebrow{font-size:11px;letter-spacing:.14em;text-transform:uppercase;color:var(--accent);font-weight:600;display:flex;align-items:center;gap:12px}
.eyebrow.rule::before{content:"";width:30px;height:1.5px;background:var(--accent)}
/* header */
.site-header{position:absolute;top:0;left:0;right:0;height:75px;border-bottom:1px solid var(--line);background:var(--paper)}
.brand{position:absolute;left:318px;top:26px;font-family:var(--serif);font-size:22px;font-weight:600;letter-spacing:-.01em}
.nav{position:absolute;left:482px;top:0;height:75px;display:flex;align-items:center;gap:30px;font-size:11.5px;letter-spacing:.08em;text-transform:uppercase;font-weight:500}
.nav .two{line-height:1.6}
.cta{position:absolute;left:850px;top:13px;width:183px;height:49px;background:var(--ink);color:#fff;font-size:10.5px;letter-spacing:.1em;font-weight:600;padding:12px 26px;line-height:1.2}
.avatar{position:absolute;left:1057px;top:22px;width:32px;height:32px;border-radius:50%;background:linear-gradient(135deg,#6b5a4c,#2f2824)}
/* hero */
.hero-eyebrow{top:186px}
.hero-title{position:absolute;left:112px;top:222px;font-family:var(--serif);font-weight:600;font-size:68px;line-height:1.05;letter-spacing:-.01em;width:640px}
.hero-copy{position:absolute;left:782px;top:254px;width:310px;font-size:16px;line-height:1.85;color:var(--body)}
.coords{position:absolute;left:782px;top:420px;font-size:9.5px;letter-spacing:.12em;color:var(--muted);display:flex;gap:14px;align-items:center}
.coords i{width:5px;height:5px;border-radius:50%;background:var(--accent)}
/* gallery */
.gallery{position:absolute;top:548px;left:0;right:0;height:1522px;background:var(--stone)}
.catalog-head{position:absolute;left:112px;right:112px;top:112px;display:flex;justify-content:space-between;align-items:center}
.catalog-label{font-size:11px;letter-spacing:.1em;font-weight:700;display:flex;align-items:center;gap:10px}
.filters{display:flex;gap:10px}
.filters span{font-size:10px;letter-spacing:.1em;font-weight:600;padding:9px 16px;background:var(--panel);color:var(--body)}
.filters span.on{background:var(--ink);color:#fff}
.plate{position:absolute;overflow:hidden;color:#fff}
.plate .tag{position:absolute;left:24px;top:24px;background:#fff;color:var(--ink);font-size:9.5px;letter-spacing:.12em;font-weight:700;padding:5px 10px}
.plate .cap{position:absolute;left:22px;right:22px;bottom:22px}
.plate .kicker{font-size:9.5px;letter-spacing:.1em;color:#e9c9a8;font-weight:600;margin-bottom:6px}
.plate h3{font-family:var(--serif);font-weight:500;font-size:24px;line-height:1.25;margin-bottom:8px}
.plate p{font-size:12.5px;line-height:1.6;color:#d9d4cc}
.shade::after{content:"";position:absolute;inset:0;background:linear-gradient(180deg,rgba(0,0,0,0) 40%,rgba(0,0,0,.72) 100%)}
.shade>*{z-index:1}
/* contact */
.contact{position:absolute;top:2070px;left:0;right:0;height:952px;background:var(--paper)}
.contact-title{position:absolute;left:112px;top:142px;font-family:var(--serif);font-weight:600;font-size:38px;line-height:1.18;width:380px}
.contact-copy{position:absolute;left:112px;top:296px;width:370px;font-size:14px;line-height:1.8;color:var(--body)}
.info-box{position:absolute;left:112px;top:433px;width:372px;height:281px;background:var(--panel);padding:30px 30px}
.info-row{display:flex;gap:14px;margin-bottom:24px}
.info-row svg{flex:none;margin-top:2px}
.info-row b{display:block;font-size:9.5px;letter-spacing:.08em;font-weight:700;margin-bottom:4px}
.info-row span{font-size:12px;color:var(--body)}
.info-row span.link{color:var(--accent)}
.guarantee{position:absolute;left:112px;top:742px;width:372px;height:104px;background:#e6e3dd;padding:24px 22px;display:flex;gap:14px}
.guarantee b{display:block;font-size:10px;letter-spacing:.08em;font-weight:700;margin-bottom:4px}
.guarantee span{font-size:12px;color:var(--body);line-height:1.6}
.form-card{position:absolute;left:544px;top:111px;width:544px;height:669px;background:var(--white);padding:44px 44px}
.form-card h2{font-family:var(--serif);font-weight:500;font-size:27px;margin:10px 0 8px}
.form-card .lead{font-size:12.5px;color:var(--body);margin-bottom:34px}
.field-label{font-size:9.5px;letter-spacing:.06em;font-weight:700;margin-bottom:10px}
.input{background:var(--stone);border:1px solid var(--line);height:44px;font-size:12px;color:#b3ada5;padding:13px 14px}
.row2{display:flex;gap:22px;margin-bottom:24px}
.row2>div{flex:1}
.select{background:var(--stone);border:1px solid var(--line);height:42px;font-size:12.5px;color:var(--ink);padding:12px 18px;margin-bottom:24px}
.textarea{height:128px;line-height:1.7;padding-top:14px;margin-bottom:28px}
.check{display:flex;gap:12px;font-size:12px;color:var(--body);line-height:1.7;margin-bottom:40px}
.check i{flex:none;width:11px;height:11px;border:1px solid var(--muted);margin-top:4px}
.submit{background:var(--ink);color:#fff;height:44px;display:flex;align-items:center;justify-content:center;gap:10px;font-size:11px;letter-spacing:.12em;font-weight:600}
/* faq */
.faq{position:absolute;top:3022px;left:0;right:0;height:981px;background:var(--stone)}
.faq .eyebrow{position:absolute;left:0;right:0;top:112px;justify-content:center}
.faq-title{position:absolute;left:0;right:0;top:142px;text-align:center;font-family:var(--serif);font-weight:600;font-size:38px;line-height:1.2}
.faq-sub{position:absolute;left:300px;right:300px;top:250px;text-align:center;font-size:14px;line-height:1.75;color:var(--body)}
.q{position:absolute;left:240px;width:720px;background:var(--white);display:flex;align-items:center;justify-content:space-between;padding:0 24px;font-family:var(--serif);font-size:20px;line-height:1.4}
.q span{width:600px}
.faq-foot{position:absolute;left:240px;width:720px;top:857px;display:flex;justify-content:space-between;font-size:12.5px;color:var(--body)}
.faq-foot b{color:var(--accent);font-size:10.5px;letter-spacing:.1em;font-weight:600}
/* footer */
.site-footer{position:absolute;top:4003px;left:0;right:0;height:403px;background:var(--paper);border-top:1px solid var(--line)}
.foot-brand{position:absolute;left:290px;top:70px;font-family:var(--serif);font-size:22px;font-weight:600}
.foot-tag{position:absolute;left:112px;top:108px;width:300px;font-size:12.5px;line-height:1.6;color:var(--body)}
.foot-vol{position:absolute;left:112px;top:160px;font-size:10px;letter-spacing:.1em;color:var(--accent);font-weight:600}
.foot-col{position:absolute;top:66px;font-size:12.5px;color:var(--body);line-height:1.5}
.foot-col h4{font-size:9.5px;letter-spacing:.08em;color:var(--ink);font-weight:700;margin-bottom:10px;line-height:1.3}
.foot-col li{list-style:none;margin-bottom:10px}
.news{position:absolute;left:865px;top:66px;width:223px}
.news h4{font-size:9.5px;letter-spacing:.08em;font-weight:700;margin-bottom:8px}
.news p{font-size:12px;line-height:1.6;color:var(--body);margin-bottom:22px}
.news .mail{display:flex;justify-content:space-between;border-bottom:1px solid var(--ink);font-size:11.5px;color:#b3ada5;padding-bottom:6px}
.news small{display:block;font-size:9.5px;letter-spacing:.08em;color:var(--muted);margin-top:10px;line-height:1.5}
.legal{position:absolute;left:112px;right:112px;top:316px;border-top:1px solid var(--line)}
.legal .copy{position:absolute;left:0;top:24px;width:300px;font-size:12px;line-height:1.6;color:var(--body)}
.legal .links{position:absolute;left:360px;top:24px;width:560px;display:flex;flex-wrap:wrap;justify-content:center;column-gap:36px;row-gap:10px;font-size:10px;letter-spacing:.1em;font-weight:600;color:var(--body);list-style:none}
.legal .links li{white-space:nowrap}
</style>
</head>
<body>

<header class="site-header">
  <div class="brand">Trelvanox482</div>
  <nav class="nav">
    <span>Home</span><span>Books</span><span>About</span><span class="two">Gallery &amp;<br>Contact</span>
  </nav>
  <div class="cta">ACQUIRE THE<br>SERIES</div>
  <div class="avatar" role="img" aria-label="Account portrait"></div>
</header>

<section class="hero">
  <div class="wrap hero-eyebrow eyebrow rule" style="position:absolute">Archive &amp; Inquiries</div>
  <h1 class="hero-title">Visual Chronicles of the Sea &amp; Direct Inquiries.</h1>
  <p class="hero-copy">A curated photographic inspection of maritime craft, close-quarters harbor geometry, letterpress book production, and direct lines to our editorial desk.</p>
  <div class="coords"><span>LAT 38°14'52" N</span><i></i><span>LON 74°06'21" W</span></div>
</section>

<section class="gallery">
  <div class="catalog-head">
    <div class="catalog-label">
      <svg width="14" height="12" viewBox="0 0 14 12"><rect x="1" y="2.5" width="12" height="8.5" fill="none" stroke="#b4511f" stroke-width="1.3"/><circle cx="7" cy="6.7" r="2.2" fill="none" stroke="#b4511f" stroke-width="1.3"/><rect x="4.5" y="0.8" width="5" height="1.8" fill="#b4511f"/></svg>
      PLATE CATALOG INDEX
    </div>
    <div class="filters"><span class="on">ALL PLATES</span><span>MONOGRAPHS &amp; BINDING</span><span>VESSEL HANDLING</span><span>HARBOR LIGHT</span></div>
  </div>

  <div class="plate shade" style="left:112px;top:224px;width:640px;height:400px;background:radial-gradient(circle at 55% 35%,#3b4f74,#1d2a44 60%,#151a24)" role="img" aria-label="Navy gilded leather book titled The Craft of Mooring beside a brass compass">
    <div class="tag">PLATE 01 · ARCHIVE</div>
    <div class="cap"><div class="kicker">GILDED LEATHER EDITION</div><h3>The Craft of Mooring: Precision, Wind &amp; Current</h3><p>Gold-foiled navigational cartography set upon royal navy leather with blind debossed hull lines.</p></div>
  </div>
  <div class="plate shade" style="left:782px;top:224px;width:306px;height:380px;background:linear-gradient(160deg,#9fb1c0,#56636e 45%,#232a33)" role="img" aria-label="Portrait of a master mariner at a marina">
    <div class="tag">PLATE 02 · SEAMANSHIP</div>
    <div class="cap"><div class="kicker">AUTHOR &amp; MASTER MARINER</div><h3 style="font-size:21px">Captain Edmund Harrow</h3><p>Forty years on tidal currents, coastal bars, and close-quarters maneuvers.</p></div>
  </div>

  <div class="plate shade" style="left:112px;top:654px;width:306px;height:382px;background:linear-gradient(150deg,#8e7456,#3c3226 45%,#1f2a22)" role="img" aria-label="Dark green cloth book titled Quayside Disciplines on a desk">
    <div class="tag">PLATE 03 · MONOGRAPH</div>
    <div class="cap"><div class="kicker">ARCHIVAL CLOTH EDITION</div><h3 style="font-size:20px">Quayside Disciplines</h3><p>Gilded brass bitts, cleat diagrams, and gold-foil title typography.</p></div>
  </div>
  <div class="plate shade" style="left:446px;top:654px;width:642px;height:400px;background:radial-gradient(circle at 50% 40%,#b5532f,#7d2f1a 60%,#3b1d14)" role="img" aria-label="Terracotta book titled Steady Helm in the Squall with an embossed ocean wave">
    <div class="tag">PLATE 04 · SPECIAL ISSUE</div>
    <div class="cap"><div class="kicker">TERRACOTTA &amp; GILT</div><h3>Steady Helm in the Squall: Heavy Weather</h3><p>Embossed ocean swell crest with crisis maneuvering protocols for gale-force approaches.</p></div>
  </div>

  <div class="plate shade" style="left:112px;top:1083px;width:473px;height:326px;background:linear-gradient(180deg,#a7aaa6,#6d6a62 45%,#3d3328)" role="img" aria-label="Coiled rope on a bronze cleat on teak decking">
    <div class="tag">PLATE 05 · HARDWARE</div>
    <div class="cap"><div class="kicker">MOORING CRAFT</div><h3 style="font-size:20px">Teak Decking &amp; Hand-Turned Bronze</h3><p>Mooring hardware precision during predawn departure trials.</p></div>
  </div>
  <div class="plate shade" style="left:615px;top:1083px;width:473px;height:326px;background:linear-gradient(150deg,#d8bb8e,#9a7650 50%,#4a3524)" role="img" aria-label="Nautical chart with dividers and compass tools">
    <div class="tag">PLATE 06 · CARTOGRAPHY</div>
    <div class="cap"><div class="kicker">NAVIGATION DESKS</div><h3 style="font-size:20px">Hydrographic Soundings &amp; Compass Lines</h3><p>Plotting drift vectors across Port Alder channel approaches.</p></div>
  </div>
</section>

<section class="contact">
  <div class="eyebrow rule" style="position:absolute;left:112px;top:112px">Get in Touch</div>
  <h2 class="contact-title">Direct Dispatch with the Atelier &amp; Captain’s Desk.</h2>
  <p class="contact-copy">Whether securing complete collector folios, commissioning bespoke yacht club seminars, or seeking navigational consults, our press keepers welcome correspondence.</p>

  <div class="info-box">
    <div class="info-row">
      <svg width="14" height="16" viewBox="0 0 14 16"><path d="M7 15s5.5-5.4 5.5-9A5.5 5.5 0 0 0 1.5 6c0 3.6 5.5 9 5.5 9z" fill="none" stroke="#b4511f" stroke-width="1.4"/><circle cx="7" cy="6" r="1.8" fill="none" stroke="#b4511f" stroke-width="1.4"/></svg>
      <div><b>EDITORIAL OFFICE &amp; ATELIER</b><span>22 Wharfside Lane, Port Alder, RI 02871</span></div>
    </div>
    <div class="info-row">
      <svg width="15" height="12" viewBox="0 0 15 12"><rect x="1" y="1" width="13" height="10" fill="none" stroke="#b4511f" stroke-width="1.4"/><path d="M1 1l6.5 5.5L14 1" fill="none" stroke="#b4511f" stroke-width="1.4"/></svg>
      <div><b>DIRECT DISPATCH</b><span class="link">dispatch@trelvanox482.com</span></div>
    </div>
    <div class="info-row">
      <svg width="15" height="12" viewBox="0 0 15 12"><rect x="1" y="1" width="13" height="10" fill="none" stroke="#b4511f" stroke-width="1.4"/><rect x="3.5" y="3.5" width="4" height="3.5" fill="#b4511f"/></svg>
      <div><b>PRESS &amp; LITERARY RIGHTS</b><span class="link">press@trelvanox482.com</span></div>
    </div>
    <div class="info-row">
      <svg width="15" height="15" viewBox="0 0 15 15"><circle cx="7.5" cy="7.5" r="6.3" fill="none" stroke="#b4511f" stroke-width="1.4"/><path d="M7.5 4v3.8l2.5 1.5" fill="none" stroke="#b4511f" stroke-width="1.4"/></svg>
      <div><b>DISPATCH &amp; ARCHIVE HOURS</b><span>Monday – Friday, 09:00 – 17:00 EST</span></div>
    </div>
  </div>

  <div class="guarantee">
    <svg width="22" height="22" viewBox="0 0 22 22" style="flex:none;margin-top:6px"><circle cx="11" cy="11" r="9" fill="none" stroke="#141210" stroke-width="1.6"/><path d="M6.8 11.2l2.8 2.8 5.6-5.6" fill="none" stroke="#141210" stroke-width="1.6"/></svg>
    <div><b>RESPONSE GUARANTEE</b><span>All correspondence reviewed by our publishing team within 24 nautical hours.</span></div>
  </div>

  <form class="form-card">
    <div class="eyebrow">Official Registry</div>
    <h2>Inquiry Transmission</h2>
    <p class="lead">Please provide thorough harbor details or order specifications below.</p>
    <div class="row2">
      <div><div class="field-label">FULL NAME / VESSEL REGISTRY *</div><div class="input">Commodore E. Vance / S.V. W.</div></div>
      <div><div class="field-label">EMAIL ADDRESS *</div><div class="input">vance@alderyachtclub.org</div></div>
    </div>
    <div class="field-label">INQUIRY CLASSIFICATION *</div>
    <div class="select">Monograph &amp; Collector Folio Acquisition</div>
    <div class="field-label">MESSAGE OR HARBOR SPECIFICATION *</div>
    <div class="input textarea">Detail your vessel loa, beam, marina berth constraints, or specific monograph distribution requirements...</div>
    <div class="check"><i></i><span>Receive the weekly <b style="color:var(--ink);font-weight:600">Harbor Dispatch</b>: private notes on tidal geometry, offshore seamanship, and private release monographs.</span></div>
    <div class="submit">SEND INQUIRY TO THE CAPTAIN’S DESK
      <svg width="12" height="10" viewBox="0 0 12 10"><path d="M1 5h9M6.5 1.5L10 5l-3.5 3.5" fill="none" stroke="#fff" stroke-width="1.4"/></svg>
    </div>
  </form>
</section>

<section class="faq">
  <div class="eyebrow">Protocol &amp; Logistics</div>
  <h2 class="faq-title">Frequently Answered Harbor<br>Inquiries.</h2>
  <p class="faq-sub">Essential details regarding global monograph dispatch, custom bookbinding, and institutional acquisitions.</p>

  <div class="q" style="top:347px;height:73px"><span>How are international collector editions packed and insured?</span><svg width="12" height="8" viewBox="0 0 12 8"><path d="M1.5 1.5L6 6l4.5-4.5" fill="none" stroke="#141210" stroke-width="1.6"/></svg></div>
  <div class="q" style="top:437px;height:103px"><span>Are institutional discounts available for yacht clubs and naval academies?</span><svg width="12" height="8" viewBox="0 0 12 8"><path d="M1.5 1.5L6 6l4.5-4.5" fill="none" stroke="#141210" stroke-width="1.6"/></svg></div>
  <div class="q" style="top:555px;height:102px"><span>Can we commission personalized bookbinding and monogramming?</span><svg width="12" height="8" viewBox="0 0 12 8"><path d="M1.5 1.5L6 6l4.5-4.5" fill="none" stroke="#141210" stroke-width="1.6"/></svg></div>
  <div class="q" style="top:672px;height:103px"><span>How do I arrange a harbor maneuver masterclass with Captain Harrow?</span><svg width="12" height="8" viewBox="0 0 12 8"><path d="M1.5 1.5L6 6l4.5-4.5" fill="none" stroke="#141210" stroke-width="1.6"/></svg></div>

  <div class="faq-foot"><span>Require specialized diplomatic or superyacht procurement?</span><b>INQUIRE DIRECTLY VIA DISPATCH DESK →</b></div>
</section>

<footer class="site-footer">
  <div class="foot-brand">Trelvanox482</div>
  <p class="foot-tag">Maritime &amp; Literary Press — Master Class Seamanship, Literature &amp; Harbor Command.</p>
  <div class="foot-vol">ARCHIVAL VOLUME III · EST. 2024</div>

  <div class="foot-col" style="left:447px;width:90px"><h4>THE EDITIONS</h4><ul><li>Volume I</li><li>Volume II</li><li>Collector Folio</li><li>Field Guides</li></ul></div>
  <div class="foot-col" style="left:548px;width:90px"><h4>THE PRESS</h4><ul><li>Monograph</li><li>Philosophy</li><li>Patrons</li><li>Curator Notes</li></ul></div>
  <div class="foot-col" style="left:649px;width:95px"><h4>MONOGRAPH ARCHIVE</h4><ul><li>Plates &amp; Charts</li><li>Nautical Blueprints</li><li>Harbor Logs</li><li>Visual Gallery</li></ul></div>
  <div class="foot-col" style="left:750px;width:90px"><h4>INQUIRIES</h4><ul><li>Press &amp; Media</li><li>Harbor Master</li><li>Acquisitions</li><li>Bespoke Folios</li></ul></div>

  <div class="news">
    <h4>THE HARBOR DISPATCH</h4>
    <p>Weekly seamanship notes &amp; private release briefings.</p>
    <div class="mail"><span>Enter patron email address</span><svg width="12" height="10" viewBox="0 0 12 10"><path d="M1 5h9M6.5 1.5L10 5l-3.5 3.5" fill="none" stroke="#141210" stroke-width="1.4"/></svg></div>
    <small>Strictly reserved for archival subscribers.</small>
  </div>

  <div class="legal">
    <p class="copy">Copyright © 2025 Trelvanox482 Press. All rights reserved.</p>
    <ul class="links"><li>PRIVACY POLICY</li><li>TERMS OF SERVICE</li><li>SHIPPING &amp; MONOGRAPH DISPATCH</li><li>ACCESSIBILITY STATEMENT</li></ul>
  </div>
</footer>

</body>
</html>
```